Bravilo - a brand new platform for targetted offers

Hello there, pixel guild!
As a new business we want to build a mobile web site (that later will be converted to mobile app) that will allow our customer to find great offers in their area provided by our partners.
What we'd like to get from you is a design of several mobile web site pages (screens). For the color choice we were considering unobtrusive combination of white, black and one of the extra colors: purple, green (shades ranging from green apple to mint) or cherry red. Most of the pages will contain images (offers) made by partners with unpredictable color combinations, so our main design should stay minimalist enough to keep customers attention to these images. The pages (screens) are as follows.
1. Welcome screen
- Product logo image
- Short text to thank customers for their choice
- Checkbox with text to accept Terms and Conditions (with link to them)
- Button to continue that is grayed out before the checkbox above is checked
2. List of offers (main screen)
- Header: search bar + 2 icon buttons: location button and menu button
- Info box with a link to profile screen to indicate that authorization is recommended
- Offers: a list of images headed with partner's icon and name aligned left and timer (clock icon + time) aligned right
- Menu: as it's planned, when menu button is pressed, a hover menu from the right is open to display a list of available screens
3. Partner's details and offers
- Header: Partner's name and back button
- Partner's full width logo image
- Short description text of a partner company (up to, say, 500 characters)
- Contact buttons with appropriate icons: "visit their web page" button, call button, location button, like/dislike buttons
- List of their offers as full-width images
- Selected offer should, also, show an "open-down" box with description aligned left and a button to use the offer aligned right
4. Favorites
- Header: Back button, screen name, filter button to open a hover screen to filter by location and other fields
- List of favorite partners with their icon and name aligned left and buttons to "subscribe"/"unsubscribe" (one button) and remove from favorites aligned right
5. Blacklist
- Same as favorites, with just "subscribe"/"unsubscribe" omitted
6. History
- List of taken offers displayed same way as on main screen with actual usage date instead of time remaining
7. Profile
- Header: Back button and screen name
- Rows of inputs for customer to define her age, gender, etc and/or authenticate by Tornquist, Velbox, etc.
8. Terms and Conitions
- Text of ToS
9. Language
- List of rows to choose a desired language
As this is our first try of PixelGuild platform, please, don't hesitate to ask more questions or correct us on our order. If it feels like there are too many screens requested ahead, please, start with the first few with the intention to complete all of them when we choose you as a winner.
Thank you in advance for your cooperation!

```html
<!DOCTYPE html>
<html lang="en">
<head>
<meta charset="utf-8">
<title>Bravilo – mobile screens</title>
<link rel="stylesheet" href="https://fonts.googleapis.com/css2?family=Raleway:wght@400;500;600;700;800&display=swap">
<style>
:root{
  --frame:#8a0fb4;
  --purple:#8a0fb4;
  --green:#1c5e1f;
  --ink:#141414;
  --grey-bg:#ececec;
  --grey-line:#dcdcdc;
  --text:#6e6e6e;
  --white:#ffffff;
}
*{box-sizing:border-box;margin:0;padding:0}
html,body{width:713px;height:1200px;overflow:hidden;background:var(--white);font-family:Raleway,sans-serif}
.board{position:relative;width:713px;height:1200px;border:5px solid var(--frame);background:var(--white);overflow:hidden}
.section-title{position:absolute;font:700 7.5px Raleway,sans-serif;color:var(--ink);text-decoration:underline;text-underline-offset:1.5px}

.screen{position:absolute;width:117px;background:var(--white);overflow:hidden;box-shadow:0 0 0 .6px #e2e2e2}
.topbar{position:absolute;left:0;top:0;width:100%;height:13px;background:var(--ink);display:flex;align-items:center}
.topbar .brand{flex:1;padding-left:4px;font:800 6px Raleway,sans-serif;color:var(--white);letter-spacing:.2px}
.topbar .search{width:38px;height:8px;display:flex;align-items:center;justify-content:space-between;padding:0 2px;font:500 3.4px Raleway,sans-serif;color:#cfcfcf;border-right:.5px solid #444}
.topbar .pin{width:11px;display:flex;justify-content:center}
.topbar .menu-btn{width:13px;height:13px;background:var(--purple);display:flex;align-items:center;justify-content:center}

.subbar{position:absolute;left:0;top:13px;width:100%;height:12px;background:var(--grey-bg);display:flex;align-items:center;justify-content:center;font:700 4.6px Raleway,sans-serif;color:var(--ink);letter-spacing:.2px}
.subbar .back{position:absolute;left:0;top:0;height:12px;width:15px;background:var(--green);clip-path:polygon(0 0,70% 0,100% 50%,70% 100%,0 100%);display:flex;align-items:center;padding-left:2.5px}
.subbar .filter{position:absolute;right:0;top:0;width:13px;height:12px;background:#d6d6d6;display:flex;align-items:center;justify-content:center}

.footer{position:absolute;left:0;bottom:0;width:100%;height:12px;background:var(--ink);display:flex;align-items:center;padding-left:9px;font:500 3.2px Raleway,sans-serif;color:var(--white)}

.photo{position:absolute;left:8px;width:101px;height:53px}
.photo.shoe{background:radial-gradient(ellipse at 50% 55%,#b2502a 0 30%,#d9cbb5 62%,#c9b89b)}
.photo.watch{background:radial-gradient(circle at 32% 50%,#9a9a9a 0 14%,#2a2a2a 30%,#0e0e0e 60%,#3a3a3a)}
.photo.bag{background:radial-gradient(ellipse at 48% 55%,#b0602c 0 32%,#e7ddd0 66%,#f1ece5)}
.photo.laces{background:linear-gradient(135deg,#c9c3bc,#3a2c26 55%,#7d756c)}
.badge-special{position:absolute;right:4px;top:3px;width:12px;height:12px;border-radius:50%;background:#e0141b}

.meta{position:absolute;left:8px;width:101px;height:12px;display:flex;align-items:center}
.meta .partner{flex:1;line-height:1}
.meta .partner b{display:block;font:800 4.4px Raleway,sans-serif;color:var(--ink)}
.meta .partner span{display:block;font:500 3.2px Raleway,sans-serif;color:var(--text);margin-top:1px}
.meta .clock{width:9px;height:9px;border-radius:50%;background:var(--grey-bg);display:flex;align-items:center;justify-content:center;margin-right:5px}
.timer{display:flex;align-items:flex-start;gap:2.5px}
.timer .unit{text-align:center;line-height:1}
.timer .unit b{display:block;font:700 5.4px Raleway,sans-serif;color:var(--ink)}
.timer .unit span{display:block;font:500 3px Raleway,sans-serif;color:var(--text);margin-top:.8px}
.timer .sep{font:700 5px Raleway,sans-serif;color:var(--ink);line-height:1}

.heading{position:absolute;left:0;width:100%;text-align:center;font:700 7.2px Raleway,sans-serif;color:var(--ink);letter-spacing:.2px}
.heading::after{content:"";display:block;width:12px;height:1px;background:var(--purple);margin:2.5px auto 0}
.divider{position:absolute;left:8px;width:101px;height:.6px;background:var(--grey-line)}
.spinner{position:absolute;left:50%;width:14px;height:14px;margin-left:-7px}

.pill{display:inline-flex;align-items:center;justify-content:center;border-radius:6px;font:700 3.6px Raleway,sans-serif;color:var(--white);letter-spacing:.1px}

/* welcome */
.welcome-photo{position:absolute;left:0;top:110px;width:100%;height:81px;background:linear-gradient(180deg,#9aa3a0 0%,#7a7f7c 45%,#4f5552 100%)}
.bubble{position:absolute;left:0;top:19px;width:100%;height:101px;background:var(--green);border-radius:12px;text-align:center;color:var(--white);padding:10px 8px 0}
.bubble::after{content:"";position:absolute;left:28px;bottom:-17px;border-left:2px solid transparent;border-right:10px solid transparent;border-top:18px solid var(--green)}
.bubble h1{font:700 9px Raleway,sans-serif}
.bubble p{font:500 4px/1.75 Raleway,sans-serif;margin-top:4px}
.bubble .terms{margin-top:4px;font:500 4px Raleway,sans-serif;display:flex;align-items:center;justify-content:center;gap:2px}
.bubble .terms u{text-underline-offset:.8px}
.bubble .submit{margin-top:6px;width:37px;height:11px;background:var(--ink);font-size:4.6px}

/* info box */
.info{position:absolute;left:8px;top:27px;width:101px;height:72px;background:var(--grey-bg);text-align:center;padding-top:7px}
.info p{font:500 3.6px/1.75 Raleway,sans-serif;color:var(--text);padding:0 4px;margin-top:4px}
.info .pill{background:var(--green);width:36px;height:9px;margin-top:4px;font-size:3.2px}

/* slide menu */
.slide-menu{position:absolute;left:50px;top:13px;width:67px;height:119px;background:#232323;padding-top:8px}
.slide-menu li{list-style:none;height:11.2px;display:flex;align-items:center;padding-left:8px;font:500 3.8px Raleway,sans-serif;color:var(--white)}
.slide-menu li::before{content:"»";margin-right:5px;font-size:4px}
.topbar .close{width:13px;display:flex;justify-content:center;margin-right:20px}

/* partner */
.desc-head{position:absolute;left:10px;font:700 4.4px Raleway,sans-serif;color:var(--purple)}
.partner-mark{position:absolute;right:8px;font:800 6px Raleway,sans-serif;color:var(--ink)}
.copy{position:absolute;left:10px;width:97px;font:500 3.75px/1.95 Raleway,sans-serif;color:var(--text)}
.copy p+p{margin-top:3px}
.actions{position:absolute;left:10px;display:flex;align-items:center;gap:3px}
.actions .pill{background:var(--purple);height:8px;padding:0 4px;gap:2px}
.icon-circle{width:8px;height:8px;border-radius:50%;border:.5px solid var(--grey-line);display:flex;align-items:center;justify-content:center}

.dropdown{position:absolute;left:8px;width:101px;height:169px;background:#161616;padding:10px 7px 0 7px;color:var(--white)}
.dropdown h3{font:700 4.8px Raleway,sans-serif;text-decoration:underline;text-underline-offset:1px}
.dropdown p{font:500 3.9px/1.9 Raleway,sans-serif;width:52px;margin-top:5px}
.dropdown .pill{position:absolute;right:6px;top:19px;width:34px;height:11px;background:var(--purple);font-size:4px}

/* favorites */
.fav-card{position:absolute;left:3px;width:111px;height:36px;border:.6px solid var(--grey-line);padding:5px 0 0 9px}
.fav-card .name{display:flex;align-items:center;gap:2px;height:12px;font:800 3.8px Raleway,sans-serif;color:var(--ink)}
.fav-card .name i{display:block;width:6px;height:6px;border-radius:50%;background:#3a3a3a}
.fav-card .row{display:flex;gap:4px;margin-top:5px}
.fav-card .sub{height:7px;width:31px;background:var(--purple);border-radius:1px;font-size:3px}
.fav-card .remove{height:7px;width:53px;background:#dedede;color:#444;border-radius:1px;font-size:3px}
</style>
</head>
<body>
<svg width="0" height="0" style="position:absolute" aria-hidden="true">
  <defs>
    <symbol id="i-search" viewBox="0 0 10 10"><circle cx="4" cy="4" r="3" fill="none" stroke="#fff" stroke-width="1.4"/><path d="M6.3 6.3 9 9" stroke="#fff" stroke-width="1.4"/></symbol>
    <symbol id="i-pin" viewBox="0 0 10 12"><path d="M5 11.5S1 7 1 4.5a4 4 0 0 1 8 0C9 7 5 11.5 5 11.5z" fill="none" stroke="currentColor" stroke-width="1"/><circle cx="5" cy="4.5" r="1.4" fill="none" stroke="currentColor" stroke-width="1"/></symbol>
    <symbol id="i-menu" viewBox="0 0 10 8"><path d="M0 1h10M0 4h10M0 7h10" stroke="#fff" stroke-width="1.3"/></symbol>
    <symbol id="i-clock" viewBox="0 0 10 10"><circle cx="5" cy="5" r="4" fill="none" stroke="#8a0fb4" stroke-width="1.2"/><path d="M5 2.6V5l1.7 1" fill="none" stroke="#8a0fb4" stroke-width="1.1"/></symbol>
    <symbol id="i-back" viewBox="0 0 10 10"><circle cx="5" cy="5" r="4.2" fill="none" stroke="#fff" stroke-width="1"/><path d="M6.8 5H3.3M4.8 3.3 3.2 5l1.6 1.7" fill="none" stroke="#fff" stroke-width="1"/></symbol>
    <symbol id="i-phone" viewBox="0 0 10 10"><path d="M2.5 1.2 4 3 3.1 4.1c.6 1.3 1.5 2.2 2.8 2.8L7 6l1.8 1.5-.8 1.3C4.6 8.8 1.2 5.4 1.2 2z" fill="none" stroke="#8a0fb4" stroke-width=".9"/></symbol>
    <symbol id="i-thumb" viewBox="0 0 10 10"><path d="M1 4.5h2V9H1zM3 4.5 5 1c1 0 1.3.7 1 1.8L5.7 4H8.5c.6 0 1 .5.8 1.1L8.3 8.4c-.1.4-.5.6-.9.6H3" fill="none" stroke="#8a0fb4" stroke-width=".8"/></symbol>
    <symbol id="i-globe" viewBox="0 0 10 10"><circle cx="5" cy="5" r="4" fill="none" stroke="#fff" stroke-width="1"/><path d="M1 5h8M5 1c-2 2.5-2 5.5 0 8M5 1c2 2.5 2 5.5 0 8" fill="none" stroke="#fff" stroke-width=".8"/></symbol>
    <symbol id="i-info" viewBox="0 0 20 20"><circle cx="10" cy="10" r="9" fill="#8a0fb4"/><circle cx="10" cy="10" r="6.3" fill="none" stroke="#fff" stroke-width="1.3"/><circle cx="10" cy="6.8" r="1" fill="#fff"/><path d="M10 9v5" stroke="#fff" stroke-width="1.6"/></symbol>
    <symbol id="i-close" viewBox="0 0 10 10"><circle cx="5" cy="5" r="4.3" fill="#fff"/><path d="M3.4 3.4 6.6 6.6M6.6 3.4 3.4 6.6" stroke="#141414" stroke-width="1.1"/></symbol>
    <symbol id="i-filter" viewBox="0 0 10 10"><path d="M1 1.5h8L6 5.3V9L4 8V5.3z" fill="none" stroke="#444" stroke-width=".9"/></symbol>
    <symbol id="i-check" viewBox="0 0 10 10"><rect x="1" y="1.5" width="7" height="7" fill="none" stroke="#fff" stroke-width="1"/><path d="M2.8 5 4.6 6.8 9 1.8" fill="none" stroke="#fff" stroke-width="1.2"/></symbol>
    <symbol id="i-spinner" viewBox="0 0 20 20"><g stroke-width="1.8" stroke-linecap="round">
      <path d="M10 2v4" stroke="#222"/><path d="M15.7 4.3 12.8 7.2" stroke="#333"/><path d="M18 10h-4" stroke="#555"/><path d="M15.7 15.7 12.8 12.8" stroke="#777"/>
      <path d="M10 18v-4" stroke="#999"/><path d="M4.3 15.7 7.2 12.8" stroke="#aaa"/><path d="M2 10h4" stroke="#bbb"/><path d="M4.3 4.3 7.2 7.2" stroke="#ccc"/></g></symbol>
  </defs>
</svg>

<main class="board">

  <h2 class="section-title" style="left:64px;top:30px">Welcome screen</h2>
  <h2 class="section-title" style="left:314px;top:30px">List of offers</h2>
  <h2 class="section-title" style="left:55px;top:293px">Partner's details and offers</h2>
  <h2 class="section-title" style="left:410px;top:582px">Favorites</h2>

  <!-- Welcome -->
  <section class="screen" style="left:149px;top:53px;height:203px">
    <div class="welcome-photo" role="img" aria-label="Photo of a young woman reading offers on her phone outdoors"></div>
    <header class="topbar">
      <span class="brand">BRAVILO</span>
      <span class="search">Search<svg width="4" height="4"><use href="#i-search"/></svg></span>
      <span class="pin" style="color:#fff"><svg width="4" height="5"><use href="#i-pin"/></svg></span>
      <span class="menu-btn"><svg width="5" height="4"><use href="#i-menu"/></svg></span>
    </header>
    <div class="bubble">
      <h1>Thank You.</h1>
      <p>Sed ut perspiciatis unde omnis iste natus error sit vore totam rem apa quae ventore veritatis</p>
      <div class="terms"><svg width="4.5" height="4.5"><use href="#i-check"/></svg><u>Accept Terms and Conditions</u></div>
      <span class="pill submit">SUBMIT</span>
    </div>
    <footer class="footer">Copyrights 2018 @ Bravilo All Rights Reserved</footer>
  </section>

  <!-- List of offers -->
  <section class="screen" style="left:410px;top:53px;height:509px">
    <header class="topbar">
      <span class="brand">BRAVILO</span>
      <span class="search">Search<svg width="4" height="4"><use href="#i-search"/></svg></span>
      <span class="pin" style="color:#fff"><svg width="4" height="5"><use href="#i-pin"/></svg></span>
      <span class="menu-btn"><svg width="5" height="4"><use href="#i-menu"/></svg></span>
    </header>
    <div class="info">
      <svg width="17" height="17"><use href="#i-info"/></svg>
      <p>Sed ut perspiciatis unde omnis iste natus error sit voluptatem accusantium dolore ab illore ve ab illore ve ab illore ve ab illore ve totam rem aperieaque ipsa quae ab illore.</p>
      <span class="pill">GET A PROFILE</span>
    </div>
    <h3 class="heading" style="top:130px">OFFERS</h3>
    <div class="photo shoe" style="top:153px" role="img" aria-label="Brown leather oxford shoe"></div>
    <div class="meta" style="top:214px"><div class="partner"><b>ardent</b><span>Ardent</span></div><span class="clock"><svg width="5" height="5"><use href="#i-clock"/></svg></span><div class="timer"><div class="unit"><b>13</b><span>Hrs</span></div><span class="sep">:</span><div class="unit"><b>36</b><span>Mins</span></div><span class="sep">:</span><div class="unit"><b>08</b><span>Secs</span></div></div></div>
    <div class="photo watch" style="top:245px" role="img" aria-label="Wristwatch resting on a laptop keyboard"><span class="badge-special"></span></div>
    <div class="meta" style="top:306px"><div class="partner"><b>swift now</b><span>Swift Now</span></div><span class="clock"><svg width="5" height="5"><use href="#i-clock"/></svg></span><div class="timer"><div class="unit"><b>13</b><span>Hrs</span></div><span class="sep">:</span><div class="unit"><b>36</b><span>Mins</span></div><span class="sep">:</span><div class="unit"><b>08</b><span>Secs</span></div></div></div>
    <div class="photo bag" style="top:337px" role="img" aria-label="Tan leather studded handbag"></div>
    <div class="meta" style="top:398px"><div class="partner"><b>lumo stick</b><span>Lumo Stick</span></div><span class="clock"><svg width="5" height="5"><use href="#i-clock"/></svg></span><div class="timer"><div class="unit"><b>13</b><span>Hrs</span></div><span class="sep">:</span><div class="unit"><b>36</b><span>Mins</span></div><span class="sep">:</span><div class="unit"><b>08</b><span>Secs</span></div></div></div>
    <div class="divider" style="top:431px"></div>
    <svg class="spinner" style="top:451px"><use href="#i-spinner"/></svg>
    <footer class="footer">Copyrights 2018 @ Bravilo All Rights Reserved</footer>
  </section>

  <!-- List of offers with menu open -->
  <section class="screen" style="left:543px;top:53px;height:509px">
    <header class="topbar">
      <span class="brand">BRAVILO</span>
      <span class="close"><svg width="5" height="5"><use href="#i-close"/></svg></span>
      <span class="menu-btn" style="margin-left:auto"><svg width="5" height="4"><use href="#i-menu"/></svg></span>
    </header>
    <div class="info">
      <svg width="17" height="17"><use href="#i-info"/></svg>
      <p>Sed ut perspiciatis unde omnis iste natus error sit voluptatem accusantium dolore ab illore ve ab illore ve ab illore ve ab illore ve totam rem aperieaque ipsa quae ab illore.</p>
      <span class="pill">GET A PROFILE</span>
    </div>
    <h3 class="heading" style="top:130px">OFFERS</h3>
    <div class="photo shoe" style="top:153px" role="img" aria-label="Brown leather oxford shoe"></div>
    <div class="meta" style="top:214px"><div class="partner"><b>ardent</b><span>Ardent</span></div><span class="clock"><svg width="5" height="5"><use href="#i-clock"/></svg></span><div class="timer"><div class="unit"><b>13</b><span>Hrs</span></div><span class="sep">:</span><div class="unit"><b>36</b><span>Mins</span></div><span class="sep">:</span><div class="unit"><b>08</b><span>Secs</span></div></div></div>
    <div class="photo watch" style="top:245px" role="img" aria-label="Wristwatch resting on a laptop keyboard"><span class="badge-special"></span></div>
    <div class="meta" style="top:306px"><div class="partner"><b>swift now</b><span>Swift Now</span></div><span class="clock"><svg width="5" height="5"><use href="#i-clock"/></svg></span><div class="timer"><div class="unit"><b>13</b><span>Hrs</span></div><span class="sep">:</span><div class="unit"><b>36</b><span>Mins</span></div><span class="sep">:</span><div class="unit"><b>08</b><span>Secs</span></div></div></div>
    <div class="photo bag" style="top:337px" role="img" aria-label="Tan leather studded handbag"></div>
    <div class="meta" style="top:398px"><div class="partner"><b>lumo stick</b><span>Lumo Stick</span></div><span class="clock"><svg width="5" height="5"><use href="#i-clock"/></svg></span><div class="timer"><div class="unit"><b>13</b><span>Hrs</span></div><span class="sep">:</span><div class="unit"><b>36</b><span>Mins</span></div><span class="sep">:</span><div class="unit"><b>08</b><span>Secs</span></div></div></div>
    <div class="divider" style="top:431px"></div>
    <svg class="spinner" style="top:451px"><use href="#i-spinner"/></svg>
    <nav class="slide-menu">
      <ul>
        <li>Welcome</li><li>List of offers</li><li>Partner's details</li><li>Favorites</li><li>Blacklist</li><li>History</li><li>Profile</li><li>Terms and Conditions</li><li>Language</li>
      </ul>
    </nav>
    <footer class="footer">Copyrights 2018 @ Bravilo All Rights Reserved</footer>
  </section>

  <!-- Partner details -->
  <section class="screen" style="left:149px;top:316px;height:748px">
    <header class="topbar">
      <span class="brand">BRAVILO</span>
      <span class="search">Search<svg width="4" height="4"><use href="#i-search"/></svg></span>
      <span class="pin" style="color:#fff"><svg width="4" height="5"><use href="#i-pin"/></svg></span>
      <span class="menu-btn"><svg width="5" height="4"><use href="#i-menu"/></svg></span>
    </header>
    <div class="subbar"><span class="back"><svg width="6" height="6"><use href="#i-back"/></svg></span>ARDENT</div>
    <div class="photo laces" style="top:38px;height:54px" role="img" aria-label="Person tying the laces of dark leather shoes"></div>
    <span class="desc-head" style="top:106px">DESCRIPTION</span>
    <span class="partner-mark" style="top:100px">ardent</span>
    <div class="copy" style="top:115px">
      <p>Sed ut perspiciatis unde omnis iste natus error sit voluptatem accusantium dolore ab illore ve ab illore ve ab illore ve ab illore ut perspiciatis unde omnis iste natus error sit voluptatem accusantium doloremque laudantiotam rem aperiam.</p>
      <p>Aaque ipsa quae ab illo inventore veritatis et quasi architecto beatae vitae dicta sunt explicabo. Nemo enim ipsam voluptatem quia voluptas sit aspernatur aut odit aut fugit, sed quia consequuntur magni dolores eos qui ratione voluptatem sequi nesciunt. Neque porro quisquam est, qui dolorem ipsum quia dolor sit amet, consectetur, adipisci velit, sed quia non numquam eius modi tempora incidunt ut labore et dolore magnam aliquamore ve totam rem aperieaque ipsa quae ab illore.</p>
      <p>Nemo enim ipsam voluptatem quia voluptas sit aspernatur aut odit aut fugit, sed quia consequuntur magni dolores eos qui ratione.</p>
    </div>
    <div class="actions" style="top:287px">
      <span class="pill"><svg width="3.5" height="3.5"><use href="#i-globe"/></svg>VISIT THEIR WEB PAGE</span>
      <span class="icon-circle"><svg width="4" height="4"><use href="#i-phone"/></svg></span>
      <span class="icon-circle" style="color:var(--purple)"><svg width="3.5" height="4"><use href="#i-pin"/></svg></span>
      <span class="icon-circle"><svg width="4" height="4"><use href="#i-thumb"/></svg></span>
    </div>
    <div class="divider" style="top:311px"></div>
    <h3 class="heading" style="top:330px">OFFERS</h3>
    <div class="photo shoe" style="top:355px" role="img" aria-label="Brown leather oxford shoe"></div>
    <div class="meta" style="top:417px"><div class="partner"><b>ardent</b><span>Ardent</span></div><span class="clock"><svg width="5" height="5"><use href="#i-clock"/></svg></span><div class="timer"><div class="unit"><b>13</b><span>Hrs</span></div><span class="sep">:</span><div class="unit"><b>36</b><span>Mins</span></div><span class="sep">:</span><div class="unit"><b>08</b><span>Secs</span></div></div></div>
    <div class="photo watch" style="top:447px" role="img" aria-label="Wristwatch resting on a laptop keyboard"><span class="badge-special"></span></div>
    <div class="meta" style="top:509px"><div class="partner"><b>ardent</b><span>Ardent</span></div><span class="clock"><svg width="5" height="5"><use href="#i-clock"/></svg></span><div class="timer"><div class="unit"><b>13</b><span>Hrs</span></div><span class="sep">:</span><div class="unit"><b>36</b><span>Mins</span></div><span class="sep">:</span><div class="unit"><b>08</b><span>Secs</span></div></div></div>
    <div class="photo bag" style="top:538px" role="img" aria-label="Tan leather studded handbag"></div>
    <div class="meta" style="top:600px"><div class="partner"><b>ardent</b><span>Ardent</span></div><span class="clock"><svg width="5" height="5"><use href="#i-clock"/></svg></span><div class="timer"><div class="unit"><b>13</b><span>Hrs</span></div><span class="sep">:</span><div class="unit"><b>36</b><span>Mins</span></div><span class="sep">:</span><div class="unit"><b>08</b><span>Secs</span></div></div></div>
    <svg class="spinner" style="top:646px"><use href="#i-spinner"/></svg>
    <footer class="footer">Copyrights 2018 @ Bravilo All Rights Reserved</footer>
  </section>

  <!-- Partner details, offer opened -->
  <section class="screen" style="left:276px;top:316px;height:748px">
    <header class="topbar">
      <span class="brand">BRAVILO</span>
      <span class="search">Search<svg width="4" height="4"><use href="#i-search"/></svg></span>
      <span class="pin" style="color:#fff"><svg width="4" height="5"><use href="#i-pin"/></svg></span>
      <span class="menu-btn"><svg width="5" height="4"><use href="#i-menu"/></svg></span>
    </header>
    <div class="subbar"><span class="back"><svg width="6" height="6"><use href="#i-back"/></svg></span>ARDENT</div>
    <div class="photo laces" style="top:38px;height:54px" role="img" aria-label="Person tying the laces of dark leather shoes"></div>
    <span class="desc-head" style="top:106px">DESCRIPTION</span>
    <span class="partner-mark" style="top:100px">ardent</span>
    <div class="copy" style="top:115px">
      <p>Sed ut perspiciatis unde omnis iste natus error sit voluptatem accusantium dolore ab illore ve ab illore ve ab illore ve ab illore ut perspiciatis unde omnis iste natus error sit voluptatem accusantium doloremque laudantiotam rem aperiam.</p>
      <p>Aaque ipsa quae ab illo inventore veritatis et quasi architecto beatae vitae dicta sunt explicabo. Nemo enim ipsam voluptatem quia voluptas sit aspernatur aut odit aut fugit, sed quia consequuntur magni dolores eos qui ratione voluptatem sequi nesciunt. Neque porro quisquam est, qui dolorem ipsum quia dolor sit amet, consectetur, adipisci velit, sed quia non numquam eius modi tempora incidunt ut labore et dolore magnam aliquamore ve totam rem aperieaque ipsa quae ab illore.</p>
      <p>Nemo enim ipsam voluptatem quia voluptas sit aspernatur aut odit aut fugit, sed quia consequuntur magni dolores eos qui ratione.</p>
    </div>
    <div class="actions" style="top:287px">
      <span class="pill"><svg width="3.5" height="3.5"><use href="#i-globe"/></svg>VISIT THEIR WEB PAGE</span>
      <span class="icon-circle"><svg width="4" height="4"><use href="#i-phone"/></svg></span>
      <span class="icon-circle" style="color:var(--purple)"><svg width="3.5" height="4"><use href="#i-pin"/></svg></span>
      <span class="icon-circle"><svg width="4" height="4"><use href="#i-thumb"/></svg></span>
    </div>
    <div class="divider" style="top:311px"></div>
    <h3 class="heading" style="top:330px">OFFERS</h3>
    <div class="photo shoe" style="top:355px" role="img" aria-label="Brown leather oxford shoe"></div>
    <div class="meta" style="top:417px"><div class="partner"><b>ardent</b><span>Ardent</span></div><span class="clock"><svg width="5" height="5"><use href="#i-clock"/></svg></span><div class="timer"><div class="unit"><b>13</b><span>Hrs</span></div><span class="sep">:</span><div class="unit"><b>36</b><span>Mins</span></div><span class="sep">:</span><div class="unit"><b>08</b><span>Secs</span></div></div></div>
    <div class="dropdown" style="top:445px">
      <h3>DESCRIPTION</h3>
      <span class="pill">SHOP NOW</span>
      <p>Aaque ipsa quae ab illo inventore veritatis et quasi architecto beatae vitae dicta sunt explicabo. Nemo enim ipsam voluptatem quia voluptas sit aspernatur. Odit aut fugit, sed quia consequuntur magni dolores eos qui ratione voluptatem sequi nesciunt. Neque porro quisquam est, qui dolorem ipsum quia dolor sit amet.</p>
    </div>
    <svg class="spinner" style="top:646px"><use href="#i-spinner"/></svg>
    <footer class="footer">Copyrights 2018 @ Bravilo All Rights Reserved</footer>
  </section>

  <!-- Favorites -->
  <section class="screen" style="left:504px;top:602px;height:490px">
    <header class="topbar">
      <span class="brand">BRAVILO</span>
      <span class="search">Search<svg width="4" height="4"><use href="#i-search"/></svg></span>
      <span class="pin" style="color:#fff"><svg width="4" height="5"><use href="#i-pin"/></svg></span>
      <span class="menu-btn"><svg width="5" height="4"><use href="#i-menu"/></svg></span>
    </header>
    <div class="subbar"><span class="back"><svg width="6" height="6"><use href="#i-back"/></svg></span>FAVORITES<span class="filter"><svg width="5" height="5"><use href="#i-filter"/></svg></span></div>
    <div class="fav-card" style="top:40px"><div class="name"><i></i>Stelmar</div><div class="row"><span class="pill sub">SUBSCRIBE</span><span class="pill remove">REMOVE FROM FAVORITES</span></div></div>
    <div class="fav-card" style="top:83px"><div class="name"><i></i>Kestra</div><div class="row"><span class="pill sub">SUBSCRIBE</span><span class="pill remove">REMOVE FROM FAVORITES</span></div></div>
    <div class="fav-card" style="top:126px"><div class="name"><i></i>Stelmar</div><div class="row"><span class="pill sub">SUBSCRIBE</span><span class="pill remove">REMOVE FROM FAVORITES</span></div></div>
    <div class="fav-card" style="top:169px"><div class="name"><i></i>Vantor</div><div class="row"><span class="pill sub">SUBSCRIBE</span><span class="pill remove">REMOVE FROM FAVORITES</span></div></div>
    <div class="fav-card" style="top:212px"><div class="name"><i></i>Halden Group</div><div class="row"><span class="pill sub">SUBSCRIBE</span><span class="pill remove">REMOVE FROM FAVORITES</span></div></div>
    <div class="fav-card" style="top:255px"><div class="name"><i></i>Norvane Expo</div><div class="row"><span class="pill sub">SUBSCRIBE</span><span class="pill remove">REMOVE FROM FAVORITES</span></div></div>
    <div class="fav-card" style="top:298px"><div class="name"><i></i>Ostra</div><div class="row"><span class="pill sub">SUBSCRIBE</span><span class="pill remove">REMOVE FROM FAVORITES</span></div></div>
    <div class="fav-card" style="top:341px"><div class="name"><i></i>Corvel Aid</div><div class="row"><span class="pill sub">SUBSCRIBE</span><span class="pill remove">REMOVE FROM FAVORITES</span></div></div>
    <svg class="spinner" style="top:402px"><use href="#i-spinner"/></svg>
    <footer class="footer">Copyrights 2018 @ Bravilo All Rights Reserved</footer>
  </section>

</main>
</body>
</html>
```